Business Card Design for general contractor or developer

General Contractors. We build new buildings as well as redesign and/or remodel existing buildings. Mostly residential, but we want to expand to commercial as well, so we want the design not to be residential specific.We want the design to be modern, but necessarily minimalistic. A monogram type is also a consideration, but would like to see all ideas.

Target Market(s)

Real estate investors, homeowners, future homeowners, commercial building owners

Industry/Entity Type

Contractor

Contact Information for Business Card

BRIMCOVE Developers Corp, 2917 NE 88th Avenue Suite 412 Coral Springs, FL 33071, Darren Kopec, (305) 555-0148, darren@brimcovedev.example

Font styles to use
Other font styles liked:
• Modern type font

Requirements
Must have
• Must be modern looking
Nice to have
• Metallic type or a standout feature
Should not have
• Tools, floorplans

```html
<!DOCTYPE html>
<html lang="en">
<head>
<meta charset="utf-8">
<title>BRIMCOVE Developers Corp – Business Card</title>
<link rel="stylesheet" href="https://fonts.googleapis.com/css2?family=Archivo:wght@800&family=Archivo+Narrow:wght@700&family=Tinos&display=swap">
<style>
  :root {
    --page: #ffffff;
    --navy: #0a2a66;
    --blue-deep: #0d3f9c;
    --blue: #1b63d1;
    --blue-light: #5fa6f0;
    --ray: rgba(200, 230, 255, 0.28);
    --steel-dark: #8d9399;
    --steel: #c9cdd1;
    --steel-light: #f4f5f6;
    --ink: #0b0b0b;
    --type-light: #ffffff;
  }
  * { margin: 0; padding: 0; box-sizing: border-box; }
  html, body {
    width: 1200px;
    height: 1200px;
    overflow: hidden;
    background: var(--page);
  }
  .business-card {
    position: absolute;
    left: 50px;
    top: 275px;
    width: 1100px;
    height: 650px;
    overflow: hidden;
    background:
      radial-gradient(ellipse 70% 60% at 72% 18%, rgba(150, 205, 255, 0.55), transparent 70%),
      linear-gradient(160deg, var(--blue-deep) 0%, var(--blue) 42%, var(--blue-deep) 75%, var(--navy) 100%);
  }
  .light-rays {
    position: absolute;
    inset: 0;
    width: 100%;
    height: 100%;
  }
  .steel-band {
    position: absolute;
    left: 0;
    top: 68px;
    width: 840px;
    height: 135px;
    background: linear-gradient(180deg, var(--steel-light) 0%, var(--steel) 45%, var(--steel-dark) 58%, var(--steel) 78%, var(--steel-light) 100%);
    box-shadow: 0 3px 8px rgba(0, 0, 0, 0.35);
  }
  .trade-title {
    position: absolute;
    left: 77px;
    top: 86px;
    font-family: "Archivo", Arial, sans-serif;
    font-weight: 800;
    font-size: 60px;
    line-height: 1;
    letter-spacing: 1px;
    color: var(--ink);
  }
  .trade-services {
    position: absolute;
    left: 77px;
    top: 153px;
    font-family: "Archivo Narrow", "Arial Narrow", sans-serif;
    font-weight: 700;
    font-size: 25px;
    line-height: 1;
    color: var(--ink);
    white-space: nowrap;
  }
  .blade-emblem {
    position: absolute;
    left: 690px;
    top: 106px;
    width: 438px;
    height: 438px;
  }
  .contact-block {
    position: absolute;
    left: 63px;
    top: 240px;
    font-family: "Tinos", "Times New Roman", serif;
    color: var(--type-light);
    line-height: 1;
    white-space: nowrap;
  }
  .contact-block p { position: absolute; left: 0; }
  .company-name { top: 0; font-size: 40px; }
  .person-name { top: 68px; font-size: 28px; letter-spacing: 0.5px; }
  .phone { top: 112px; font-size: 28px; }
  .address-street { top: 172px; font-size: 29px; }
  .address-city { top: 220px; font-size: 37px; }
  .email { top: 284px; font-size: 31px; }
</style>
</head>
<body>
  <div class="business-card">
    <svg class="light-rays" viewBox="0 0 1100 650" aria-hidden="true">
      <defs>
        <linearGradient id="rayFade" x1="0" y1="0" x2="1" y2="1">
          <stop offset="0" stop-color="#d8ecff" stop-opacity="0.45"/>
          <stop offset="1" stop-color="#d8ecff" stop-opacity="0"/>
        </linearGradient>
      </defs>
      <polygon points="820,0 900,0 420,650 300,650" fill="url(#rayFade)" opacity="0.5"/>
      <polygon points="950,0 990,0 700,650 620,650" fill="url(#rayFade)" opacity="0.4"/>
      <polygon points="700,0 740,0 120,650 40,650" fill="url(#rayFade)" opacity="0.3"/>
      <polygon points="1040,0 1100,0 1100,260" fill="url(#rayFade)" opacity="0.35"/>
      <polygon points="560,0 590,0 0,520 0,470" fill="url(#rayFade)" opacity="0.25"/>
    </svg>

    <div class="steel-band"></div>
    <h1 class="trade-title">CONTRACTORS</h1>
    <p class="trade-services">new buildings, redesign/remodel existing buildings</p>

    <svg class="blade-emblem" viewBox="0 0 438 438" role="img" aria-label="Silver circular saw blade emblem with hammer and paintbrush">
      <defs>
        <radialGradient id="bladeSteel" cx="0.45" cy="0.4" r="0.6">
          <stop offset="0" stop-color="#f7f8f9"/>
          <stop offset="0.55" stop-color="#c4c9ce"/>
          <stop offset="1" stop-color="#8e959c"/>
        </radialGradient>
      </defs>
      <circle cx="219" cy="219" r="216" fill="url(#bladeSteel)"/>
    </svg>

    <div class="contact-block">
      <p class="company-name">BRIMCOVE Developers Corp</p>
      <p class="person-name">DARREN KOPEC</p>
      <p class="phone">Ph (305) 555-0148</p>
      <p class="address-street">2917 NE 88th Avenue Suite</p>
      <p class="address-city">412 Coral Springs, FL 33071</p>
      <p class="email">darren@brimcovedev.example</p>
    </div>
  </div>
</body>
</html>
```